brightquokka.net we need a webpage designed for our new product

We need a webpage designed for our new range of products from our new brand. We have had a logo designed on sketchhive (see attached) and we want to keep to this theme. Our first product is a range of affordable app controlled LED lightbulbs.

I have added some photos that we think is good inspirational material and would be good as a background to this website, but we want the site to look modern but not conventional. We would like something that makes our company look quirky not corporate.

Thats it

Target Market(s)

Our product is being stocked by big name online retailers in the UK, the page will get link through hits from our app. Our target market is gadget freaks of all ages.

Industry/Entity Type

It Company

Requirements
Must have
• We are going to need a help page, text to be uploaded next few days.

We need a contact page.

design my work on iOS and Android as most people will access page through their handset or tablet.
Should not have
• We do not want anything too corporate.

```html
<!DOCTYPE html>
<html lang="en">
<head>
<meta charset="utf-8">
<title>Brightquokka – App controlled LED bulbs</title>
<link href="https://fonts.googleapis.com/css2?family=Open+Sans:wght@400;600;700&display=swap" rel="stylesheet">
<style>
:root{
  --green:#3daf4a;
  --green-dark:#2e8a39;
  --ink:#3a3a3a;
  --muted:#555;
  --footer:#454545;
  --rule:#cfcfcf;
  --white:#fff;
}
*{box-sizing:border-box;margin:0;padding:0}
html,body{width:806px;height:1200px;overflow:hidden;background:var(--white)}
body{position:relative;font-family:"Open Sans",Arial,sans-serif;color:var(--ink)}
a{text-decoration:none}
.abs{position:absolute}

.brand{left:72px;top:38px;display:flex;align-items:center;gap:6px;font-size:14px;font-weight:700;color:var(--green)}
.brand-dot{width:12px;height:12px;border-radius:50%;background:var(--green)}
.search{left:558px;top:41px;width:171px;height:24px;background:#f1f1f1}
.search-btn{position:absolute;right:0;top:0;width:23px;height:24px;background:var(--green);display:flex;align-items:center;justify-content:center}

.nav{left:0;top:105px;width:806px;height:44px;background:var(--green)}
.nav a{position:absolute;top:0;height:44px;line-height:44px;color:var(--white);font-size:10px;font-weight:600;transform:translateX(-50%);white-space:nowrap}
.nav a.active{top:12px;height:22px;line-height:22px;padding:0 9px;background:var(--green-dark);border-radius:2px}

.hero{left:0;top:151px;width:806px;height:285px;background:linear-gradient(120deg,#6b5a48 0%,#a0483e 40%,#7a6a55 65%,#4d3f33 100%)}
.dots{right:26px;top:414px;display:flex;gap:4px}
.dots span{width:7px;height:7px;border-radius:50%;background:var(--white)}
.dots span:first-child{background:var(--green)}

.bar{height:27px;background:var(--green);color:var(--white);font-weight:700;font-size:14px;line-height:27px;padding-left:13px;border-radius:2px}
.body-text{font-size:8px;line-height:13.5px;color:var(--muted);text-align:justify}

.photo{background:linear-gradient(135deg,#8a6a4a,#c9a57a)}
.arrow{width:17px;height:17px;border-radius:50%;background:#e6e6e6;display:flex;align-items:center;justify-content:center}

.post{left:70px;width:300px;height:42px}
.post-thumb{position:absolute;left:0;top:0;width:38px;height:38px;border:1px solid #ddd;padding:3px;background:var(--white)}
.post-thumb div{width:100%;height:100%}
.post p{position:absolute;left:48px;top:6px;width:250px;font-size:7px;line-height:12px;color:#222;font-weight:400}
.sep{left:70px;width:299px;border-top:1px dashed var(--rule)}

.btn{left:551px;top:1032px;width:85px;height:29px;background:#454545;color:var(--white);font-size:10px;font-weight:600;line-height:29px;text-align:center;border-radius:2px}

.footer{left:0;top:1113px;width:806px;height:87px;background:var(--footer);border-top:4px solid var(--green)}
.footer-links{left:70px;top:1142px;font-size:8px;color:var(--white)}
.footer-links span{margin:0 4px}
.copy{left:70px;top:1168px;font-size:8px;color:var(--white)}
.social{left:626px;top:1151px;display:flex;gap:13px}
.social span{width:16px;height:16px;border-radius:50%;background:#e8e8e8}
</style>
</head>
<body>

<header>
  <div class="abs brand"><span class="brand-dot"></span>Brightquokka</div>
  <div class="abs search">
    <div class="search-btn">
      <svg width="11" height="11" viewBox="0 0 11 11"><circle cx="4.5" cy="4.5" r="3.3" fill="none" stroke="#fff" stroke-width="1.6"/><line x1="7" y1="7" x2="10" y2="10" stroke="#fff" stroke-width="1.8"/></svg>
    </div>
  </div>
</header>

<nav class="abs nav">
  <a class="active" href="#" style="left:95px">Home</a>
  <a href="#" style="left:162px">About Us</a>
  <a href="#" style="left:239px">Products</a>
  <a href="#" style="left:312px">Offers</a>
  <a href="#" style="left:376px">Blog</a>
  <a href="#" style="left:458px">Testimonials</a>
  <a href="#" style="left:548px">Location</a>
  <a href="#" style="left:637px">Contact Us</a>
  <a href="#" style="left:706px">Help</a>
</nav>

<div class="abs hero" role="img" aria-label="Photo of a shop floor full of quirky gadgets, toy cars and figures"></div>
<div class="abs dots"><span></span><span></span><span></span><span></span></div>

<section>
  <h2 class="abs bar" style="left:69px;top:464px;width:672px">Welcome to Brightquokka</h2>
  <div class="abs photo" style="left:76px;top:524px;width:109px;height:80px;background:linear-gradient(135deg,#7a5a40,#e8e2d8)" role="img" aria-label="Photo of a white ceramic figurine"></div>
  <p class="abs body-text" style="left:205px;top:522px;width:536px">Say hello to lighting with a personality. Our first range is a family of affordable LED bulbs that you run straight from your phone or tablet. Dim them, change their colour, set them to wake you gently or to flash when your team scores. Each bulb screws into a normal fitting, pairs with our free app in seconds and sips far less power than an old bulb. No hub, no wiring, no fuss. Build scenes for every room, share them with friends and let the whole house glow the way you like it. Made for gadget fans of every age who want their home to feel a little less ordinary and a lot more fun to live in every single day.</p>
  <p class="abs body-text" style="left:69px;top:617px;width:672px">You will find our bulbs at big online retailers across the UK, and you can jump here straight from the app whenever you need us. Every bulb comes in warm white or full colour, with a long life and a two year guarantee. Not sure where to start? Our Help page walks you through setup, pairing and the odd hiccup, and our Contact page puts you in touch with a real human who loves light as much as you do. We add new colours, modes and silly party tricks to the app all the time, so keep an eye on the blog for the latest updates, tips and ideas from our growing crowd of happy owners.</p>
</section>

<section>
  <h2 class="abs bar" style="left:69px;top:709px;width:672px">Our Products</h2>
  <div class="abs arrow" style="left:71px;top:792px"><svg width="7" height="8" viewBox="0 0 7 8"><path d="M5 1 2 4l3 3" fill="none" stroke="#fff" stroke-width="1.6"/></svg></div>
  <div class="abs photo" style="left:114px;top:766px;width:102px;height:69px;background:linear-gradient(135deg,#5a4a3a,#3a5aa0 50%,#a03a3a)" role="img" aria-label="Product photo"></div>
  <div class="abs photo" style="left:236px;top:766px;width:102px;height:69px;background:linear-gradient(135deg,#8a2a3a,#c83a3a 50%,#d8c040)" role="img" aria-label="Product photo"></div>
  <div class="abs photo" style="left:357px;top:766px;width:102px;height:69px;background:linear-gradient(135deg,#c08010,#e8a020 50%,#3a5aa0)" role="img" aria-label="Product photo"></div>
  <div class="abs photo" style="left:478px;top:766px;width:102px;height:69px;background:linear-gradient(135deg,#6a3a20,#8a5a3a 50%,#2a2a30)" role="img" aria-label="Product photo"></div>
  <div class="abs photo" style="left:598px;top:766px;width:102px;height:69px;background:linear-gradient(135deg,#7a4a20,#d89a50 50%,#5a3a20)" role="img" aria-label="Photo of glowing hanging lamps"></div>
  <div class="abs arrow" style="left:724px;top:792px"><svg width="7" height="8" viewBox="0 0 7 8"><path d="M2 1l3 3-3 3" fill="none" stroke="#fff" stroke-width="1.6"/></svg></div>
</section>

<section>
  <h2 class="abs bar" style="left:69px;top:883px;width:330px;padding-left:20px">Our Blog</h2>
  <div class="abs post" style="top:935px">
    <div class="post-thumb"><div style="background:linear-gradient(135deg,#7a4a20,#d89a50)" role="img" aria-label="Blog post thumbnail photo"></div></div>
    <p>Five party scenes to try tonight with your new colour bulbs, from disco flash to a calm sunset glow in any room.</p>
  </div>
  <div class="abs sep" style="top:980px"></div>
  <div class="abs post" style="top:990px">
    <div class="post-thumb"><div style="background:linear-gradient(135deg,#3a8a4a,#d04040)" role="img" aria-label="Blog post thumbnail photo"></div></div>
    <p>How a wake up light routine can make dark winter mornings easier, and how to set one up in the app in a minute.</p>
  </div>
  <div class="abs sep" style="top:1035px"></div>
  <div class="abs post" style="top:1046px">
    <div class="post-thumb"><div style="background:linear-gradient(135deg,#3a5aa0,#e0a030)" role="img" aria-label="Blog post thumbnail photo"></div></div>
    <p>App update: new colour modes, room groups and a timer that keeps the lights on while you are away from home.</p>
  </div>
</section>

<section>
  <h2 class="abs bar" style="left:433px;top:883px;width:308px;padding-left:26px">Our Offers</h2>
  <div class="abs photo" style="left:453px;top:942px;width:77px;height:116px;background:linear-gradient(180deg,#8a5a30,#5a3a25 55%,#2a2a35)" role="img" aria-label="Photo of a shop aisle lined with collectibles"></div>
  <p class="abs body-text" style="left:551px;top:938px;width:170px;font-size:8px;line-height:12.8px">Launch deal: buy three colour bulbs and get the fourth free. Fits any standard fitting and pairs with the app in seconds. Stock is limited, so light up your home before the offer ends this month.</p>
  <a class="abs btn" href="#">View More</a>
</section>

<footer class="abs footer"></footer>
<div class="abs footer-links">Home<span>|</span>About Us<span>|</span>Products<span>|</span>Offers<span>|</span>Blog<span>|</span>Testimonials<span>|</span>Location<span>|</span>Contact Us<span>|</span>Help</div>
<div class="abs copy">© Copyright 2014&nbsp; Brightquokka&nbsp; |&nbsp; All rights reserved</div>
<div class="abs social" aria-label="Social links"><span></span><span></span><span></span><span></span></div>

</body>
</html>
```